Harbrook Builders PowerPoint Presentation

We need a sales pitch in powerpoint form for a "commercial only" construction company based out of Dallas, TX. We perform commercial only construction including ground up, build to suit, white box and many others. We would like the design to match the color scheme and outlook of the website and brochure that will be attached. Also, attached you will find the old presentation we used (it's terrible). http://www.harbrookbld.example/

Target Market(s)

Commercial property managers, commercial building owners, business owners, facility managers, commercial construction managers, construction design teams

Industry/Entity Type

Construction

Requirements
Must have
• Commercial construction pictures. Company overview. Specific industries served.
Should not have
• Residential pictures. Poor quality pictures. Anything that doesn't look like the website or attached brochure.

```html
<!DOCTYPE html>
<html lang="en">
<head>
<meta charset="utf-8">
<title>Harbrook Builders – Presentation Slides</title>
<link href="https://fonts.googleapis.com/css2?family=Montserrat:wght@400;500;700;800&display=swap" rel="stylesheet">
<style>
  :root{
    --orange:#b5692a;
    --orange-deep:#a45c1f;
    --brown:#6b4523;
    --bar-light:#a86b38;
    --ink:#333335;
    --body:#3d3d3d;
    --band:#4f5b5b;
    --rule:#9a9a9a;
    --dot:#b5692a;
    --dot-hot:#f07a5a;
    --paper:#ffffff;
    --chart-bg:#faf7f5;
  }
  *{margin:0;padding:0;box-sizing:border-box}
  html,body{width:1200px;height:1034px;overflow:hidden;background:#fff}
  body{position:relative;font-family:'Montserrat',Arial,sans-serif;color:var(--body)}
  .slide{position:absolute;width:584px;height:328px;overflow:hidden;background:var(--paper);border:1px solid #eee}
  .s-about{left:10px;top:8px}
  .s-cols{left:604px;top:8px}
  .s-partner{left:10px;top:354px}
  .s-graphics{left:606px;top:354px}
  .s-cover-a{left:10px;top:702px;height:327px;border:none}
  .s-cover-b{left:610px;top:702px;height:327px;border:none}

  .top-rule{position:absolute;left:20px;top:0;width:220px;height:3px;background:var(--rule)}
  .deco{position:absolute;left:0;top:0}
  .slide-title{position:absolute;left:22px;top:27px;font-size:18px;font-weight:800;color:var(--ink);letter-spacing:-.2px}
  .slide-title span{color:var(--orange)}
  .brand{position:absolute;top:14px;right:10px;display:flex;align-items:center;gap:4px;font-size:11px;font-weight:700;color:var(--ink);letter-spacing:.2px;white-space:nowrap}
  .brand i{display:block;width:12px;height:12px;border-radius:50%;background:var(--orange)}
  .footer{position:absolute;left:0;bottom:0;width:100%;height:12px;background:var(--band);color:#fff;font-size:6.5px;line-height:12px;padding-left:6px}

  .photo{position:absolute}
  .copy{position:absolute;font-size:7.4px;line-height:12.2px;text-align:justify;color:var(--body)}
  .copy p+p{margin-top:12px}

  .about-photo{left:2px;top:80px;width:215px;height:214px;background:linear-gradient(160deg,#6d8fb8 0%,#a7b6c4 40%,#e6c93a 60%,#8c8b83 100%)}
  .about-copy{left:238px;top:80px;width:317px}

  .col-title{position:absolute;left:28px;top:78px;font-size:13px;font-weight:700;color:var(--orange)}
  .col-copy{top:97px;width:232px;line-height:14px;font-size:7.3px}
  .col-copy p+p{margin-top:14px}
  .col-a{left:28px}.col-b{left:300px}

  .badges{position:absolute;left:18px;top:108px;width:245px}
  .badge-row{display:flex;justify-content:center;gap:14px;margin-bottom:14px}
  .badge-circle{width:40px;height:40px;border-radius:50%;background:#d8d8d8}
  .badge-rect{width:54px;height:16px;background:#cfcfcf}
  .partner-copy{left:275px;top:82px;width:280px}

  .charts{position:absolute;left:10px;top:115px}

  .cover-photo{position:absolute;inset:0}
  .cover-a-photo{background:linear-gradient(180deg,#2f7fd8 0%,#7fb4ea 35%,#cfcfc8 60%,#8f8a7f 100%)}
  .cover-a-panel{position:absolute;left:0;top:0}
  .cover-b-photo{background:linear-gradient(135deg,#c17a33 0%,#b5692a 45%,#9c5a22 100%)}
  .cover-b-window{position:absolute;left:0;top:0}
  .cover-b-band{position:absolute;left:0;bottom:0;width:100%;height:12px;background:#4a4f45}
  .cover-brand{position:absolute;display:flex;align-items:center;gap:7px;color:#fff;font-weight:700;letter-spacing:.3px;white-space:nowrap}
  .cover-brand i{display:block;flex:none;border-radius:50%;background:#fff}
  .cover-title{position:absolute;color:#fff;font-weight:800;white-space:nowrap}
  .cover-text{position:absolute;color:#fff;text-align:justify}
  .a-brand{left:29px;top:128px;font-size:17px}
  .a-brand i{width:30px;height:30px}
  .a-title{left:37px;top:178px;font-size:15.5px}
  .a-text{left:37px;top:197px;width:193px;font-size:8.5px;line-height:12.2px}
  .b-brand{left:282px;top:110px;font-size:18px}
  .b-brand i{width:30px;height:30px}
  .b-title{left:282px;top:150px;font-size:25px}
  .b-text{left:282px;top:189px;width:275px;font-size:8.5px;line-height:12.3px}
</style>
</head>
<body>

<!-- About -->
<section class="slide s-about">
  <svg class="deco" width="584" height="328" viewBox="0 0 584 328" aria-hidden="true">
    <path d="M380 0 Q470 70 584 80" fill="none" stroke="#f3ead9" stroke-width="1"/>
    <path d="M470 230 Q520 300 584 310" fill="none" stroke="#f3ead9" stroke-width="1"/>
    <circle cx="440" cy="50" r="5" fill="var(--dot)"/>
    <circle cx="469" cy="308" r="5" fill="var(--dot)"/>
  </svg>
  <div class="top-rule"></div>
  <h2 class="slide-title">ABOUT <span>INTRODUCTION</span></h2>
  <div class="brand"><i></i>HARBROOK BUILDERS</div>
  <div class="photo about-photo" role="img" aria-label="Construction worker holding a yellow hard hat and rolled plans in front of a building site"></div>
  <div class="copy about-copy">
    <p>Lorem Ipsum is simply dummy text of the printing and typesetting industry. Lorem Ipsum has been the industry's standard dummy text ever since the 1500s, when an unknown printer took a galley of type and scrambled it to make a type specimen book. It has survived not only five centuries, but also the leap into electronic typesetting, remaining essentially unchanged. It was popularised in the 1960s with the release of Letraset sheets containing Lorem Ipsum passages, and more recently with desktop publishing software like Aldus PageMaker including versions of Lorem Ipsum.</p>
    <p>Lorem Ipsum is simply dummy text of the printing and typesetting industry. Lorem Ipsum has been the industry's standard dummy text ever since the 1500s, when an unknown printer took a galley of type and scrambled it to make a type specimen book. It has survived not only five centuries, but also the leap into electronic typesetting, remaining essentially unchanged.</p>
    <p>It was popularised in the 1960s with the release of Letraset sheets containing Lorem Ipsum passages, and more recently with desktop publishing software like Aldus PageMaker including versions of Lorem Ipsum.</p>
  </div>
  <div class="footer">Copyright @Text</div>
</section>

<!-- Two columns -->
<section class="slide s-cols">
  <svg class="deco" width="584" height="328" viewBox="0 0 584 328" aria-hidden="true">
    <path d="M370 0 Q460 70 584 80" fill="none" stroke="#f3ead9" stroke-width="1"/>
    <circle cx="441" cy="50" r="5" fill="var(--dot)"/>
    <circle cx="470" cy="308" r="5" fill="var(--dot-hot)"/>
  </svg>
  <div class="top-rule"></div>
  <h2 class="slide-title">TWO <span>COL CONTENT</span></h2>
  <div class="brand"><i></i>HARBROOK BUILDERS</div>
  <h3 class="col-title">Col Title</h3>
  <div class="copy col-copy col-a">
    <p>Lorem Ipsum is simply dummy text of the printing and typesetting industry. Lorem Ipsum has been the industry's standard dummy text ever since the 1500s, when an unknown printer took a galley of type and scrambled it to make a type specimen book. It has survived not only five centuries, but also the leap into electronic typesetting, remaining essentially unchanged. Lorem Ipsum is simply dummy text of the printing and typesetting industry.</p>
    <p>Lorem Ipsum has been the industry's standard dummy text ever since the 1500s, when an unknown printer took a galley of type and scrambled it to make a type specimen book. It has survived not only five centuries, but also the leap into electronic typesetting, remaining essentially unchanged.</p>
  </div>
  <div class="copy col-copy col-b">
    <p>Lorem Ipsum is simply dummy text of the printing and typesetting industry. Lorem Ipsum has been the industry's standard dummy text ever since the 1500s, when an unknown printer took a galley of type and scrambled it to make a type specimen book. It has survived not only five centuries, but also the leap into electronic typesetting, remaining essentially unchanged. Lorem Ipsum is simply dummy text of the printing and typesetting industry.</p>
    <p>Lorem Ipsum has been the industry's standard dummy text ever since the 1500s, when an unknown printer took a galley of type and scrambled it to make a type specimen book. It has survived not only five centuries, but also the leap into electronic typesetting, remaining essentially unchanged.</p>
  </div>
  <div class="footer">Copyright @Text</div>
</section>

<!-- Partners -->
<section class="slide s-partner">
  <svg class="deco" width="584" height="328" viewBox="0 0 584 328" aria-hidden="true">
    <path d="M370 0 Q470 80 584 70" fill="none" stroke="#f5ecc8" stroke-width="1"/>
    <path d="M440 50 Q420 200 469 308" fill="none" stroke="#f5ecc8" stroke-width="1"/>
    <circle cx="440" cy="50" r="5" fill="var(--dot)"/>
    <circle cx="469" cy="308" r="5" fill="var(--dot-hot)"/>
  </svg>
  <div class="top-rule"></div>
  <h2 class="slide-title">OUR <span>PARTNER</span></h2>
  <div class="brand"><i></i>HARBROOK BUILDERS</div>
  <div class="badges" aria-label="Partner badges">
    <div class="badge-row"><span class="badge-circle"></span><span class="badge-circle"></span><span class="badge-circle"></span><span class="badge-circle"></span></div>
    <div class="badge-row"><span class="badge-rect"></span><span class="badge-rect"></span><span class="badge-rect"></span><span class="badge-rect"></span></div>
    <div class="badge-row"><span class="badge-rect"></span><span class="badge-rect" style="width:80px"></span></div>
  </div>
  <div class="copy partner-copy">
    <p>Lorem Ipsum is simply dummy text of the printing and typesetting industry. Lorem Ipsum has been the industry's standard dummy text ever since the 1500s, when an unknown printer took a galley of type and scrambled it to make a type specimen book. It has survived not only five centuries, but also the leap into electronic typesetting, remaining essentially unchanged. It was popularised in the 1960s with the release of Letraset sheets containing Lorem Ipsum passages, and more recently with desktop publishing software like Aldus PageMaker including versions of Lorem Ipsum.</p>
    <p>Lorem Ipsum is simply dummy text of the printing and typesetting industry. Lorem Ipsum has been the industry's standard dummy text ever since the 1500s, when an unknown printer took a galley of type and scrambled it to make a type specimen book. It has survived not only five centuries, but also the leap into electronic typesetting, remaining essentially unchanged.</p>
  </div>
  <div class="footer">Copyright @Text</div>
</section>

<!-- Graphics -->
<section class="slide s-graphics">
  <div class="top-rule"></div>
  <h2 class="slide-title">OUR <span>GRAPHICS</span></h2>
  <div class="brand"><i></i>HARBROOK BUILDERS</div>
  <svg class="charts" width="570" height="170" viewBox="0 0 570 170" font-family="Montserrat, Arial, sans-serif" font-size="6" fill="#c77a4a">
    <rect x="14" y="0" width="550" height="168" fill="var(--chart-bg)"/>
    <g id="chart-1" transform="translate(22,5)">
      <text x="0" y="4">5</text><text x="0" y="31">4</text><text x="0" y="58">3</text><text x="0" y="85">2</text><text x="0" y="112">1</text><text x="0" y="139">0</text>
      <line x1="10" y1="0" x2="10" y2="137" stroke="#555" stroke-width=".6"/><line x1="10" y1="137" x2="105" y2="137" stroke="#555" stroke-width=".6"/>
      <rect x="14" y="110" width="22" height="27" fill="var(--bar-light)"/><rect x="36" y="96.5" width="22" height="40.5" fill="var(--brown)"/><rect x="58" y="83" width="22" height="54" fill="var(--bar-light)"/><rect x="80" y="56" width="22" height="81" fill="var(--bar-light)"/>
    </g>
    <g id="chart-2" transform="translate(161,5)">
      <text x="0" y="4">5</text><text x="0" y="31">4</text><text x="0" y="58">3</text><text x="0" y="85">2</text><text x="0" y="112">1</text><text x="0" y="139">0</text>
      <line x1="10" y1="0" x2="10" y2="137" stroke="#555" stroke-width=".6"/><line x1="10" y1="137" x2="105" y2="137" stroke="#555" stroke-width=".6"/>
      <rect x="14" y="129" width="22" height="8" fill="var(--bar-light)"/><rect x="36" y="104.6" width="22" height="32.4" fill="var(--brown)"/><rect x="58" y="110" width="22" height="27" fill="var(--bar-light)"/><rect x="80" y="93.8" width="22" height="43.2" fill="var(--bar-light)"/>
    </g>
    <g id="chart-3" transform="translate(300,5)">
      <text x="0" y="4">5</text><text x="0" y="31">4</text><text x="0" y="58">3</text><text x="0" y="85">2</text><text x="0" y="112">1</text><text x="0" y="139">0</text>
      <line x1="10" y1="0" x2="10" y2="137" stroke="#555" stroke-width=".6"/><line x1="10" y1="137" x2="105" y2="137" stroke="#555" stroke-width=".6"/>
      <rect x="14" y="2" width="22" height="135" fill="var(--bar-light)"/><rect x="36" y="66.8" width="22" height="70.2" fill="var(--brown)"/><rect x="58" y="42.5" width="22" height="94.5" fill="var(--bar-light)"/><rect x="80" y="88.4" width="22" height="48.6" fill="var(--bar-light)"/>
    </g>
    <g id="chart-4" transform="translate(439,5)">
      <text x="0" y="4">5</text><text x="0" y="31">4</text><text x="0" y="58">3</text><text x="0" y="85">2</text><text x="0" y="112">1</text><text x="0" y="139">0</text>
      <line x1="10" y1="0" x2="10" y2="137" stroke="#555" stroke-width=".6"/><line x1="10" y1="137" x2="105" y2="137" stroke="#555" stroke-width=".6"/>
      <rect x="14" y="104.6" width="22" height="32.4" fill="var(--bar-light)"/><rect x="36" y="69.5" width="22" height="67.5" fill="var(--brown)"/><rect x="58" y="29" width="22" height="108" fill="var(--bar-light)"/><rect x="80" y="118.1" width="22" height="18.9" fill="var(--bar-light)"/>
    </g>
  </svg>
  <div class="footer">Copyright @Text</div>
</section>

<!-- Cover A -->
<section class="slide s-cover-a">
  <div class="cover-photo cover-a-photo" role="img" aria-label="Tower cranes over a concrete building under construction against a blue sky"></div>
  <svg class="cover-a-panel" width="584" height="327" viewBox="0 0 584 327" aria-hidden="true">
    <polygon points="0,0 193,0 323,327 0,327" fill="var(--orange)"/>
  </svg>
  <div class="cover-brand a-brand"><i></i>HARBROOK BUILDERS</div>
  <h2 class="cover-title a-title">PROJECT TITLE HERE</h2>
  <p class="cover-text a-text">Lorem Ipsum is simply dummy text of the printing and typesetting industry. Lorem Ipsum has been the industry's standard dummy text ever since the 1500s.</p>
</section>

<!-- Cover B -->
<section class="slide s-cover-b">
  <div class="cover-photo cover-b-photo" role="img" aria-label="Steel scaffolding and formwork of a construction site tinted in orange"></div>
  <svg class="cover-b-window" width="584" height="327" viewBox="0 0 584 327" role="img" aria-label="Framed view of a crane and blue scaffolding on the construction site">
    <defs>
      <linearGradient id="site-view" x1="0" y1="0" x2="0" y2="1">
        <stop offset="0" stop-color="#4f8fd6"/>
        <stop offset=".55" stop-color="#8fb3d6"/>
        <stop offset="1" stop-color="#d3a24e"/>
      </linearGradient>
    </defs>
    <path d="M0 40 Q40 0 110 5 Q30 130 120 300 L0 310 Z" fill="url(#site-view)"/>
    <path d="M130 5 Q230 0 265 120 Q280 230 225 300 L150 305 Q210 160 130 5 Z" fill="url(#site-view)"/>
  </svg>
  <div class="cover-b-band"></div>
  <div class="cover-brand b-brand"><i></i>HARBROOK BUILDERS</div>
  <h2 class="cover-title b-title">PROJECT TITLE HERE</h2>
  <p class="cover-text b-text">Lorem Ipsum is simply dummy text of the printing and typesetting industry. Lorem Ipsum has been the industry's standard dummy text ever since the 1500s.</p>
</section>

</body>
</html>
```